Business Card Design Project

I am looking for a business card design for my custom Audio/Video & Contracting business named Brelvora Systems Inc. We do not currently have a corporate logo so you should not feel constrained to work around an existing design. Your design should be elegant and clean while artistically conveying that we are a technology company. We provide A/V services for the commercial and residential markets and contracting services for residential remodeling and home theater construction. We do not have a particular color that we are looking to design around so feel free to be creative.

To get references of the kind of work that we do and design inspiration please visit the following sites:

http://www.quenlamark.us
www.morvethpro.com
www.feltonbraxa.com

Reason: I think we are getting close on a couple of the designs and want to give additional time to get tweaks done and to resubmit your designs.

Target Market(s)

Most of our clients are very wealthy and have been exposed to premium brand names in every aspect of their lives, (ie. - luxury autos, estate sized homes, fine jewelery and clothes) and your design needs to convey that same level of excellent design that they are used to.

Industry/Entity Type

Residential

Requirements
Should not have
• An extensive use of the color RED.

```html
<!DOCTYPE html>
<html lang="en">
<head>
<meta charset="utf-8">
<title>Brelvora Systems Inc. — Business Card</title>
<link rel="stylesheet" href="https://fonts.googleapis.com/css2?family=Stint+Ultra+Condensed&family=Cormorant+Garamond:ital,wght@1,500&display=swap">
<style>
  :root {
    --page-bg: #f4f8fc;
    --card-bg: #d9e8f5;
    --card-edge: #c3d4e4;
    --brand-blue: #3d7fdc;
    --title-grey: #8e8e8e;
    --body-ink: #2b2b2b;
  }
  * { box-sizing: border-box; margin: 0; padding: 0; }
  html, body {
    width: 1200px;
    height: 900px;
    overflow: hidden;
    background: var(--page-bg);
  }
  .canvas {
    position: relative;
    width: 1200px;
    height: 900px;
  }
  .card {
    position: absolute;
    width: 620px;
    height: 380px;
    background: var(--card-bg);
    border: 1px solid var(--card-edge);
  }
  .card-front { left: 70px; top: 55px; }
  .card-back { left: 510px; top: 465px; }

  .brand-lockup {
    position: absolute;
    left: 0; right: 0; top: 150px;
    display: flex;
    align-items: center;
    justify-content: center;
    gap: 16px;
  }
  .brand-dot {
    width: 22px; height: 22px;
    border-radius: 50%;
    background: var(--brand-blue);
  }
  .brand-name {
    font-family: "Stint Ultra Condensed", serif;
    font-size: 64px;
    line-height: 1;
    color: var(--brand-blue);
  }

  .service-title {
    position: absolute;
    left: 0; right: 0; top: 30px;
    text-align: center;
    font-family: "Stint Ultra Condensed", serif;
    font-size: 58px;
    line-height: 1;
    color: var(--title-grey);
    letter-spacing: 1px;
  }
  .service-summary {
    position: absolute;
    left: 40px; right: 40px; top: 100px;
    text-align: center;
    font-family: "Cormorant Garamond", serif;
    font-style: italic;
    font-weight: 500;
    font-size: 15px;
    line-height: 1.3;
    color: var(--body-ink);
  }
  .contact-list {
    position: absolute;
    left: 170px; top: 165px;
    list-style: none;
    font-family: "Stint Ultra Condensed", serif;
    font-size: 36px;
    line-height: 1;
    color: var(--brand-blue);
  }
  .contact-row {
    display: flex;
    align-items: flex-end;
    justify-content: flex-end;
    gap: 8px;
    height: 38px;
  }
  .contact-rule {
    width: 150px;
    border-bottom: 3px dashed var(--brand-blue);
    margin-bottom: 6px;
  }
  .brand-mini {
    position: absolute;
    right: 26px; bottom: 26px;
    display: flex;
    align-items: center;
    gap: 6px;
  }
  .brand-mini .brand-dot { width: 9px; height: 9px; }
  .brand-mini .brand-name { font-size: 24px; }
</style>
</head>
<body>
<main class="canvas">
  <section class="card card-front" aria-label="Card front">
    <div class="brand-lockup">
      <span class="brand-dot"></span>
      <span class="brand-name">Brelvora Systems Inc.</span>
    </div>
  </section>

  <section class="card card-back" aria-label="Card back">
    <h1 class="service-title">Audio/Video &amp; Contracting</h1>
    <p class="service-summary">We provide A/V services for the commercial and residential markets<br>and contracting services for residential remodeling and home theater construction.</p>
    <ul class="contact-list">
      <li class="contact-row"><span>Tel.</span><span class="contact-rule"></span></li>
      <li class="contact-row"><span>Fax</span><span class="contact-rule"></span></li>
      <li class="contact-row"><span>e-mail</span><span class="contact-rule"></span></li>
      <li class="contact-row"><span>Address</span><span class="contact-rule"></span></li>
    </ul>
    <div class="brand-mini">
      <span class="brand-dot"></span>
      <span class="brand-name">Brelvora Systems Inc.</span>
    </div>
  </section>
</main>
</body>
</html>
```